Non Profit raising scholarship funds needs flyer for Golf Tournament

We need a flyer for our upcoming golf tournament. Proceeds to will help to benefit our Pathway builders learning grant fund.

Title: 2019 O-RamVT Golf Tournament
Location: Brindle Oaks Links
Date: May 15, 2019
Registration: $175 individual, $700 foursome
Sponsorships starting at $250
Benefiting O-RamVT and the Pathway Builders Learning Grant Fund

Target Market(s)

Design and Construction industry professionals

Industry/Entity Type

Construction

Font styles to use
Serif
Sans Serif

Colors

Designer to choose colors to be used in the design.

Requirements
Must have
• Title, date, location, registration info, sponsor info, benefit info, logo
Nice to have
• I like the retro look of some golf flyers, but it's not necessary
Should not have
• .

```html
<!DOCTYPE html>
<html lang="en">
<head>
<meta charset="utf-8">
<title>2019 O-RamVT Golf Tournament</title>
<link rel="stylesheet" href="https://fonts.googleapis.com/css2?family=Open+Sans:wght@300;400;600;700;800&family=Roboto+Condensed:wght@700;900&display=swap">
<style>
  :root {
    --page-purple: #3f3a86;
    --brand-purple: #463f90;
    --brand-green: #80b22b;
    --grass-light: #8fbf3a;
    --grass-dark: #2f5a14;
    --ink: #0d0d0d;
    --paper: #ffffff;
    --ball-ghost: #ececec;
    --logo-grey: #555555;
  }
  html, body {
    margin: 0;
    width: 1200px;
    height: 1200px;
    overflow: hidden;
    background: var(--page-purple);
  }
  .flyer {
    position: absolute;
    left: 132px;
    top: 0;
    width: 936px;
    height: 1200px;
  }
  .flyer svg { display: block; }
  .sans { font-family: "Open Sans", Arial, sans-serif; }
  .condensed { font-family: "Roboto Condensed", "Arial Narrow", sans-serif; }
</style>
</head>
<body>
<div class="flyer">
<svg width="936" height="1200" viewBox="0 0 936 1200" xmlns="http://www.w3.org/2000/svg">
  <defs>
    <linearGradient id="grass" x1="0" y1="0" x2="0" y2="1">
      <stop offset="0" stop-color="var(--grass-light)"/>
      <stop offset="1" stop-color="var(--grass-dark)"/>
    </linearGradient>
  </defs>

  <!-- paper -->
  <rect class="paper" width="936" height="1200" fill="var(--paper)"/>

  <!-- faint golf ball decoration -->
  <circle class="ball-ghost" role="img" aria-label="Faint golf ball decoration" cx="500" cy="40" r="160" fill="var(--ball-ghost)"/>

  <!-- golf photo area -->
  <g class="hero-photo" role="img" aria-label="Photo of a golf ball on a red tee beside a club head on green grass">
    <rect x="0" y="400" width="936" height="612" fill="url(#grass)"/>
  </g>

  <!-- right purple swoosh -->
  <path class="swoosh-purple" d="M300,540 C500,500 720,495 936,556 L936,850 C720,690 500,600 300,540 Z" fill="var(--brand-purple)"/>

  <!-- white divider curve -->
  <path class="divider-curve" d="M0,462 C300,520 700,650 936,850" fill="none" stroke="var(--paper)" stroke-width="10"/>

  <!-- green title band -->
  <path class="band-green" d="M0,380 C350,298 700,178 936,38 L936,556 C720,495 500,500 310,540 C200,505 100,475 0,458 Z" fill="var(--brand-green)"/>

  <!-- purple stripe -->
  <path class="stripe-purple" d="M0,350 C350,262 700,130 936,-6 L936,40 C700,180 350,300 0,384 Z" fill="var(--brand-purple)"/>

  <!-- brand -->
  <g class="brand">
    <circle cx="192" cy="80" r="62" fill="var(--brand-purple)"/>
    <text class="sans" x="192" y="210" text-anchor="middle" font-size="66" font-weight="400" fill="var(--logo-grey)">O-RamVT</text>
    <line x1="58" y1="226" x2="326" y2="226" stroke="var(--logo-grey)" stroke-width="2"/>
    <text class="sans" x="58" y="252" font-size="13" font-weight="600" fill="var(--brand-green)" textLength="300" lengthAdjust="spacingAndGlyphs">Office for Rising Ambition in Vocational Trades</text>
  </g>

  <!-- title -->
  <text class="title-year sans" x="922" y="396" text-anchor="end" font-size="88" font-weight="800" fill="var(--paper)">2019 O-RAMVT</text>
  <text class="title-event sans" x="914" y="476" text-anchor="end" font-size="76" font-weight="800" fill="var(--ink)" letter-spacing="2">GOLF TOURNAMENT</text>

  <!-- swoosh label -->
  <g class="fund-label sans" transform="translate(522,558) rotate(12)" fill="var(--paper)" font-weight="800">
    <text x="0" y="0" font-size="42" textLength="372" lengthAdjust="spacingAndGlyphs">LEARNING GRANT</text>
    <text x="204" y="54" font-size="42" letter-spacing="3">FUND</text>
  </g>

  <!-- venue and date -->
  <g class="venue sans" font-weight="800" fill="var(--ink)" stroke="var(--paper)" stroke-width="7" paint-order="stroke" stroke-linejoin="round">
    <text x="20" y="636" font-size="42" textLength="440" lengthAdjust="spacingAndGlyphs">BRINDLE OAKS LINKS</text>
    <text x="76" y="694" font-size="44" letter-spacing="-1">MAY 15, 2019</text>
  </g>

  <!-- price badges -->
  <g class="badge badge-individual">
    <circle cx="116" cy="804" r="78" fill="var(--brand-purple)"/>
    <circle cx="116" cy="804" r="64" fill="none" stroke="var(--paper)" stroke-width="2" stroke-dasharray="2 4"/>
    <text class="sans" x="116" y="820" text-anchor="middle" font-size="44" font-weight="800" fill="var(--paper)">$175</text>
  </g>
  <g class="badge badge-foursome">
    <circle cx="760" cy="872" r="78" fill="var(--brand-green)"/>
    <circle cx="760" cy="872" r="64" fill="none" stroke="var(--paper)" stroke-width="2" stroke-dasharray="2 4"/>
    <text class="sans" x="760" y="888" text-anchor="middle" font-size="44" font-weight="800" fill="var(--paper)">$700</text>
  </g>

  <!-- registration -->
  <text class="reg-individual condensed" x="208" y="824" font-size="92" font-weight="900" fill="var(--paper)" stroke="var(--brand-purple)" stroke-width="10" paint-order="stroke" stroke-linejoin="round" textLength="448" lengthAdjust="spacingAndGlyphs">INDIVIDUAL</text>
  <text class="reg-foursome condensed" x="220" y="916" font-size="92" font-weight="900" fill="var(--paper)" stroke="var(--brand-green)" stroke-width="10" paint-order="stroke" stroke-linejoin="round" textLength="448" lengthAdjust="spacingAndGlyphs">FOURSOME</text>

  <!-- footer -->
  <rect class="footer" x="0" y="1012" width="936" height="188" fill="var(--brand-purple)"/>
  <path class="sponsor-tab" d="M512,1000 L696,1000 L696,1052 Q696,1088 660,1088 L548,1088 Q512,1088 512,1052 Z" fill="var(--brand-green)"/>
  <text class="sponsor-price sans" x="604" y="1060" text-anchor="middle" font-size="54" font-weight="800" fill="var(--paper)">$250</text>
  <text class="sponsor-lead sans" x="52" y="1070" font-size="34" font-weight="300" fill="var(--paper)">SPONSORSHIPS STARTING AT</text>
  <text class="benefit-line sans" x="468" y="1126" text-anchor="middle" font-size="30" font-weight="400" fill="var(--paper)">Benefiting O-RamVT and the Pathway Builders</text>
  <text class="benefit-fund sans" x="468" y="1184" text-anchor="middle" font-size="44" font-weight="800" fill="var(--paper)" letter-spacing="1">LEARNING GRANT FUND</text>
</svg>
</div>
</body>
</html>
```